Powerpoint design for management consultant

We need a powerpoint design to use for our corporate presentations, proposal summaries and for delivering report recommendations.

Target Market(s)

Executives in Government & Private Industry

Industry/Entity Type

Consultant

Requirements
Must have
• Must use the company logo contained in the uploaded files.
Must be a powerpoint template file (.potx) that can be used with Powerpoint 2007 and later.
Must have a title slide.
Must have a purpose slide (in today's presentation we will cover ....)
Must have an agenda slide.
Must have three topic slides (topic1, topic2, topic3) as transition slides
Must support side by side comparisons
Any images used must be available royalty/ license free
Must have a summary slide.
Must have a questions slide at the end.
Must have a footer containing slide number in format of x of y.
Must have a footer containing presentation name.
Must have a footer containing the presentation date.
Must have a footer containing "confidential"
Nice to have
• The powerpoint should support the ability to represent data using infographics.
Should not have
• no tag lines or references to being management consultants. must not use custom fonts.

```html
<!DOCTYPE html>
<html lang="en">
<head>
<meta charset="utf-8">
<title>Presentation Template – Cover and Content Slides</title>
<link rel="stylesheet" href="https://fonts.googleapis.com/css2?family=Arimo:wght@400;700&family=Cabin:wght@400&family=Inter:wght@300&display=swap">
<style>
  :root {
    --stage: #e6e6e6;
    --slide: #ffffff;
    --magenta: #bf4d97;
    --orange: #f7a823;
    --orange-deep: #e5963a;
    --sky: #22bfe0;
    --cyan: #06bedb;
    --teal: #4cc3b4;
    --navy: #0e2a40;
    --ink: #111111;
    --muted: #8a8a8a;
  }
  * { margin: 0; padding: 0; box-sizing: border-box; }
  html, body { width: 1200px; height: 1000px; overflow: hidden; }
  body {
    position: relative;
    background: var(--stage);
    font-family: "Arimo", Arial, sans-serif;
  }
  .slide {
    position: absolute;
    left: 0;
    width: 720px;
    background: var(--slide);
    overflow: hidden;
  }
  .slide--cover { top: 0; height: 453px; }
  .slide--content { top: 466px; height: 534px; }
  .slide svg { position: absolute; left: 0; top: 0; }

  .brand-graphic {
    position: absolute;
    left: 0;
    background: linear-gradient(160deg, var(--magenta) 0%, var(--magenta) 35%, var(--sky) 70%, var(--teal) 100%);
    opacity: 0.9;
  }
  .slide--cover .brand-graphic { top: 5px; width: 445px; height: 244px; border-radius: 0 16px 16px 0; }
  .slide--content .brand-graphic { top: 41px; width: 100px; height: 52px; border-radius: 0 6px 6px 0; }

  .brand {
    position: absolute;
    font-family: "Arimo", Arial, sans-serif;
    font-weight: 700;
    color: var(--navy);
    letter-spacing: 0.02em;
    line-height: 1;
  }
  .slide--cover .brand { left: 458px; top: 57px; font-size: 38px; }
  .slide--content .brand { left: 107px; top: 49px; font-size: 15px; }

  .cover-title {
    position: absolute;
    left: 0; width: 720px; top: 268px;
    text-align: center;
    font-size: 26px;
    font-weight: 400;
    color: var(--ink);
  }
  .cover-date {
    position: absolute;
    left: 0; width: 720px; top: 310px;
    text-align: center;
    font-size: 16px;
    color: var(--muted);
  }
  .content-title {
    position: absolute;
    left: 0; width: 696px; top: 108px;
    text-align: center;
    font-size: 26px;
    font-weight: 400;
    color: var(--ink);
  }
  .tier-value { font-family: "Arimo", Arial, sans-serif; font-size: 13px; fill: #ffffff; }
  .tier-label { font-family: "Cabin", "Gill Sans", sans-serif; font-size: 18.5px; }

  .slide-tag {
    position: absolute;
    left: 718px;
    font-family: "Inter", "Helvetica Neue", sans-serif;
    font-weight: 300;
    font-size: 46px;
    color: #111;
    line-height: 1;
  }
  .slide-tag--cover { top: 278px; }
  .slide-tag--content { top: 696px; }
</style>
</head>
<body>

<section class="slide slide--cover">
  <div class="brand-graphic" role="img" aria-label="Decorative brand graphic in magenta, orange, blue and teal"></div>
  <div class="brand">KESTRANE</div>
  <h1 class="cover-title">Executives in Government &amp; Private Industry</h1>
  <p class="cover-date">October 3 ,2013</p>
</section>

<section class="slide slide--content">
  <div class="brand-graphic" role="img" aria-label="Small decorative brand graphic in magenta, orange, blue and teal"></div>
  <svg width="720" height="534" viewBox="0 0 720 534" aria-hidden="true">
    <polygon fill="var(--teal)" points="209,191 245,259 173,259"/>
    <polygon fill="var(--orange-deep)" points="170,264 248,264 285,335 133,335"/>
    <polygon fill="var(--cyan)" points="130,340 288,340 326,411 92,411"/>
    <polygon fill="var(--magenta)" points="90,416 328,416 366,487 52,487"/>

    <text class="tier-value" x="209" y="249" text-anchor="middle">25%</text>
    <text class="tier-value" x="209" y="305" text-anchor="middle">35%</text>
    <text class="tier-value" x="209" y="380" text-anchor="middle">45%</text>
    <text class="tier-value" x="209" y="456" text-anchor="middle">65%</text>

    <g stroke-width="1.5" fill="none">
      <line stroke="var(--teal)" x1="226" y1="222" x2="480" y2="222"/>
      <polyline stroke="var(--teal)" points="474,218 480,222 474,226"/>
      <line stroke="var(--orange-deep)" x1="266" y1="292" x2="480" y2="292"/>
      <polyline stroke="var(--orange-deep)" points="474,288 480,292 474,296"/>
      <line stroke="var(--cyan)" x1="306" y1="371" x2="480" y2="371"/>
      <polyline stroke="var(--cyan)" points="474,367 480,371 474,375"/>
      <line stroke="var(--magenta)" x1="350" y1="457" x2="480" y2="457"/>
      <polyline stroke="var(--magenta)" points="474,453 480,457 474,461"/>
    </g>

    <text class="tier-label" x="497" y="230" fill="var(--teal)">Website</text>
    <text class="tier-label" x="497" y="302" fill="var(--orange-deep)">Tablet - Website</text>
    <text class="tier-label" x="497" y="381" fill="var(--cyan)">Tablet Magazine App</text>
    <text class="tier-label" x="497" y="464" fill="var(--magenta)">Mobile Site</text>
  </svg>
  <div class="brand">KESTRANE</div>
  <h2 class="content-title">Our Audiences Access Our Content Continuously</h2>
</section>

<p class="slide-tag slide-tag--cover">&gt; Cover</p>
<p class="slide-tag slide-tag--content">&gt; Content</p>

</body>
</html>
```